Webdesign für Bedrucken Papiertaschen, Schildern etc.
Zielgruppe
Wir bedrucken Papiertaschen, Papierbeutel, Laternen, Aluplaketten, Schilder, etc. und lasern Hundemarken. Zielgruppen von Privat bis Geschäftskunden
Aufgabenstellung
Der Shop sollte ein einfacher und kostengünstiger 'printfeld'-shop werden. Wo die Kunden anhand von einem Editor Ihre Logos oder Druckvorlagen selber hochladen und/oder gestalten könne. Bisher haben die Kunden eifach ihre Bidldatei per E-Mail geschickt und wir haben diese dann weiter verarbeit.
Der Shop sollte, wenn möglich, günstig im Unterhalt sein, da wir nicht abschätzen können, wie gut diese laufen wird.
Wir haben wie 3 Bereich: 1. Papierbeutel/Taschen / 2. Stallplaketten (für z.B. Pferdesport) / 3. Diverses (Wie z.B. die Laternen, Schilder, Hundemarken, etc.)
Es würde sich um eine separate Webseite handeln. Daher ist bei Design freie Hand, eifach und klar... auch für nicht so ambitionierte Privatkunden oder kleine Unternehmen.

```html
<!DOCTYPE html>
<html lang="de">
<head>
<meta charset="utf-8">
<title>printfeld – Druckprodukte online gestalten</title>
<link rel="stylesheet" href="https://fonts.googleapis.com/css2?family=Inter:wght@400;500;600;700&family=Inter+Tight:wght@600;700;800&display=swap">
<style>
:root{
  --ink:#0f1420;
  --ink-2:#1b2130;
  --lime:#baee3f;
  --lime-soft:#eefbd2;
  --bg:#f6f7f9;
  --stage:#c4c4c4;
  --card:#ffffff;
  --line:#e6e8ec;
  --muted:#6b7280;
  --muted-2:#9aa1ac;
  --head:"Inter Tight",Inter,sans-serif;
  --body:Inter,sans-serif;
}
*{box-sizing:border-box;margin:0;padding:0}
html,body{width:1200px;height:2536px;overflow:hidden;background:var(--stage);font-family:var(--body);color:var(--ink)}
.stage{position:absolute;left:0;top:0;width:1219px;height:2576px;transform:scale(.98441);transform-origin:0 0}
.abs{position:absolute}
svg{display:block}
.ico{width:10px;height:10px;stroke:currentColor;fill:none;stroke-width:1.8;stroke-linecap:round;stroke-linejoin:round}

/* ---------- desktop ---------- */
.desk{position:absolute;left:239px;top:54px;width:928px;height:2468px;background:var(--bg);overflow:hidden}
.nav{left:78px;top:18px;width:770px;height:32px;background:#fff;border-radius:16px;box-shadow:0 2px 8px rgba(15,20,32,.06);display:flex;align-items:center;padding:0 6px 0 14px}
.brand{font-family:var(--head);font-weight:700;font-size:21px;letter-spacing:-.5px;display:flex;align-items:center;gap:5px}
.brand .dot{width:9px;height:9px;background:var(--lime);border-radius:2px}
.nav-links{margin-left:auto;display:flex;gap:18px;font-size:9.5px;color:#333;margin-right:20px}
.icon-btn{width:22px;height:22px;border:1px solid var(--line);border-radius:50%;display:flex;align-items:center;justify-content:center;margin-right:6px}
.btn{display:inline-flex;align-items:center;gap:6px;height:22px;padding:0 12px;border-radius:12px;font-size:9.5px;font-weight:600;white-space:nowrap}
.btn-dark{background:var(--ink);color:#fff}
.btn-lime{background:var(--lime);color:var(--ink)}
.btn-ghost{border:1px solid #3a4050;color:#fff}
.btn-outline{border:1px solid var(--ink);color:var(--ink)}

.hero{left:83px;top:82px;width:438px;height:316px;background:var(--ink);border-radius:16px;padding:32px 30px;color:#fff;background-image:linear-gradient(rgba(255,255,255,.035) 1px,transparent 1px),linear-gradient(90deg,rgba(255,255,255,.035) 1px,transparent 1px);background-size:24px 24px}
.pill-badge{display:inline-flex;align-items:center;gap:5px;background:#222836;border-radius:10px;padding:3px 8px;font-size:7.5px;color:#dfe3ea}
.pill-badge i{width:4px;height:4px;border-radius:50%;background:var(--lime)}
.hero h1{font-family:var(--head);font-weight:800;font-size:44px;line-height:42px;letter-spacing:-1.6px;margin-top:14px}
.hero h1 .grey{color:#8f96a3}
.hero h1 .mark{background:var(--lime);color:var(--ink);border-radius:9px;padding:0 6px;display:inline-block;line-height:40px;margin-top:2px}
.hero p{font-size:10.5px;line-height:17px;color:#c2c7d0;margin-top:16px;width:360px}
.hero .actions{display:flex;gap:8px;margin-top:18px}
.hero .btn{height:32px;padding:0 14px;border-radius:16px;font-size:10px}
.arrow-dot{width:13px;height:13px;border-radius:50%;background:var(--ink);color:var(--lime);display:flex;align-items:center;justify-content:center}
.arrow-dot .ico{width:7px;height:7px}

.mini-card{background:#fff;border:1px solid var(--line);border-radius:14px;padding:15px 14px}
.kicker{font-size:7px;letter-spacing:1.3px;font-weight:600;color:var(--muted);text-transform:uppercase}
.stars{font-size:10px;letter-spacing:1px;margin-top:46px}
.big-num{font-family:var(--head);font-weight:700;font-size:20px;margin-top:2px}
.small{font-size:7.5px;color:var(--muted);line-height:10px}
.check-card{background:var(--lime);border-radius:14px;padding:15px 14px}
.check-card .kicker{color:#4d6312}
.check-card .big-num{margin-top:48px;font-size:19px}
.check-card .small{color:var(--ink)}
.chips{display:flex;flex-wrap:wrap;gap:5px;margin-top:12px;width:250px}
.chip{display:inline-flex;align-items:center;gap:4px;border:1px solid var(--line);border-radius:10px;padding:3px 7px;font-size:7.5px}
.chip .ico{width:8px;height:8px}
.lime-link{font-size:8px;color:#8fbf1a;margin-top:14px;display:flex;gap:3px;align-items:center}

.sec-label{font-size:7.5px;letter-spacing:2px;font-weight:600;color:#9ccf25}
.sec-title{font-family:var(--head);font-weight:700;font-size:22px;letter-spacing:-.6px;margin-top:8px}
.sec-sub{font-size:9.5px;color:var(--muted);margin-top:8px}

.prod-head{left:83px;top:449px;width:761px}
.all-link{position:absolute;right:0;top:32px;font-size:8.5px;font-weight:600;display:flex;gap:4px;align-items:center}
.products{left:83px;top:516px;width:761px;display:flex;gap:13px}
.product{width:245px;height:312px;background:#fff;border:1px solid var(--line);border-radius:14px;overflow:hidden;position:relative}
.product .visual{height:184px;position:relative}
.v-bag{background:linear-gradient(160deg,#fdeac9,#ffd9a6)}
.v-plate{background:linear-gradient(160deg,#ffe1ea,#fdd3e2)}
.v-misc{background:linear-gradient(160deg,#ece8ff,#dcdcfb)}
.tag{position:absolute;left:10px;top:10px;background:#fff;border-radius:8px;padding:2px 7px;font-size:7px;font-weight:500}
.product h3{font-family:var(--head);font-size:14.5px;line-height:17px;font-weight:700;margin:16px 15px 0}
.product p{font-size:8px;line-height:12px;color:var(--muted);margin:9px 15px 0;width:210px}
.price{position:absolute;left:15px;bottom:21px;font-size:8.5px;font-weight:600}
.round{position:absolute;right:15px;bottom:16px;width:20px;height:20px;border:1px solid var(--line);border-radius:50%;display:flex;align-items:center;justify-content:center}
.round .ico{width:8px;height:8px}

.steps{left:83px;top:893px;width:761px;height:224px;background:#fff;border:1px solid var(--line);border-radius:14px;padding:26px 25px}
.steps .aside{position:absolute;right:32px;top:42px;width:232px;font-size:8.5px;line-height:12px;color:var(--muted)}
.steps .track{position:absolute;left:25px;right:25px;top:117px;height:1px;background:var(--line)}
.step{position:absolute;top:96px;width:170px}
.num{width:42px;height:42px;border:1px solid var(--line);border-radius:50%;background:#fff;display:flex;align-items:center;justify-content:center;font-family:var(--head);font-weight:700;font-size:11px}
.done{position:absolute;left:50px;top:15px;background:var(--lime);border-radius:7px;font-size:5.5px;font-weight:700;padding:2px 6px;letter-spacing:.5px}
.step h4{font-size:10.5px;font-weight:700;margin-top:15px}
.step p{font-size:8.5px;line-height:13px;color:var(--muted);margin-top:7px;width:165px}

.ed-head{left:83px;top:1180px;width:761px}
.ed-head .btn{position:absolute;right:0;top:35px;height:29px;border-radius:15px;padding:0 14px}
.editor{left:83px;top:1264px;width:761px;height:489px;background:#fff;border:1px solid var(--line);border-radius:14px;overflow:hidden}
.ed-left{position:absolute;left:0;top:0;width:161px;height:100%;border-right:1px solid var(--line)}
.ed-label{font-size:6.5px;letter-spacing:1.2px;font-weight:600;color:var(--muted)}
.tools{display:grid;grid-template-columns:68px 68px;gap:4px;margin-top:8px}
.tool{height:39px;border:1px solid var(--line);border-radius:8px;display:flex;flex-direction:column;align-items:center;justify-content:center;gap:3px;font-size:7px}
.tool.on{background:var(--lime);border-color:var(--lime)}
.swatches{display:flex;gap:5px;margin-top:9px}
.sw{width:17px;height:17px;border-radius:50%}
.layer{display:flex;align-items:center;gap:9px;font-size:7.5px;height:20px;padding:0 8px;border-radius:6px;margin:0 9px 3px}
.layer.on{background:var(--lime-soft);border:1px solid #daf29a}
.ed-mid{position:absolute;left:161px;top:0;width:426px;height:100%;background:#edeff2}
.ed-bar{height:32px;background:#fff;border-bottom:1px solid var(--line);display:flex;align-items:center;padding:0 8px;gap:8px;font-size:7.5px}
.seg{display:flex;background:#f0f1f4;border-radius:8px;padding:2px}
.seg span{padding:4px 8px;border-radius:6px;color:var(--muted)}
.seg span.on{background:#fff;color:var(--ink);font-weight:600}
.page{position:absolute;left:108px;top:113px;width:210px;height:295px;background:#fff;box-shadow:0 4px 14px rgba(0,0,0,.08)}
.page .inner{position:absolute;inset:7px;border:1px dashed #ece7cc}
.sel{position:absolute;left:85px;top:286px;width:150px;height:34px;border:1.5px solid var(--ink);background:#fff;text-align:center;font-family:var(--head);font-weight:700;font-size:12px;line-height:14px;padding-top:3px}
.sel b{position:absolute;width:4px;height:4px;background:var(--ink)}
.live{position:absolute;left:12px;bottom:12px;background:#fff;border-radius:9px;padding:3px 8px;font-size:6.5px;display:flex;gap:4px;align-items:center}
.live i{width:4px;height:4px;border-radius:50%;background:var(--lime)}
.ed-right{position:absolute;left:587px;top:0;width:174px;height:100%;padding:0 10px}
.field{border:1px solid var(--line);border-radius:6px;height:20px;font-size:7px;display:flex;align-items:center;padding:0 6px;margin-top:5px}
.pl{font-size:6px;letter-spacing:1px;font-weight:600;color:var(--muted)}
.dots{display:flex;gap:6px;margin-top:6px;flex-wrap:wrap;width:150px}
.dots i{width:14px;height:14px;border-radius:50%}

.features{left:83px;top:1833px;width:761px;display:flex;gap:11px}
.feat{flex:1;height:116px;background:#fff;border:1px solid var(--line);border-radius:14px;padding:15px}
.feat .badge{width:26px;height:26px;border-radius:8px;background:var(--ink);color:var(--lime);display:flex;align-items:center;justify-content:center}
.feat .badge .ico{width:11px;height:11px}
.feat h4{font-size:10.5px;font-weight:700;margin-top:22px}
.feat p{font-size:8.5px;line-height:12px;color:var(--muted);margin-top:8px}

.cta{left:83px;top:1989px;width:761px;height:141px;background:var(--lime);border-radius:16px;padding:40px 40px}
.cta h2{font-family:var(--head);font-weight:700;font-size:30px;line-height:30px;letter-spacing:-1px;width:330px}
.cta .actions{position:absolute;right:40px;top:56px;display:flex;gap:8px}
.cta .btn{height:29px;border-radius:15px;padding:0 14px}

.foot{left:0;top:2208px;width:928px;height:260px;background:var(--ink);color:#fff}
.foot .brand{position:absolute;left:83px;top:40px;font-size:22px}
.foot .desc{position:absolute;left:83px;top:76px;width:230px;font-size:9px;line-height:13px;color:#aeb4bf}
.foot .btn{position:absolute;left:83px;top:126px;height:24px}
.fcol{position:absolute;top:40px;font-size:9px;color:#aeb4bf}
.fcol h5{color:#fff;font-size:9px;font-weight:700;margin-bottom:12px}
.fcol div{margin-bottom:9px;display:flex;gap:6px;align-items:flex-start}
.fcol .ico{width:9px;height:9px;color:var(--lime);margin-top:1px}
.foot .bottom{position:absolute;left:83px;right:83px;top:212px;font-size:7.5px;color:#7d8593;display:flex}
.foot .bottom span+span{margin-left:14px}

/* ---------- mobile ---------- */
.mob{position:absolute;left:54px;top:54px;width:156px;height:2468px;background:var(--bg);overflow:hidden;font-size:5px}
.mob .m{position:absolute;left:10px;width:136px}
.m-nav{top:10px;height:17px;background:#fff;border-radius:9px;display:flex;align-items:center;padding:0 5px;box-shadow:0 1px 4px rgba(0,0,0,.05)}
.m-nav .brand{font-size:10px;gap:3px}
.m-nav .brand .dot{width:5px;height:5px}
.m-nav .btn{height:9px;padding:0 5px;font-size:4.5px;margin-left:auto;border-radius:5px}
.m-hero{top:41px;height:167px;background:var(--ink);border-radius:8px;padding:12px;color:#fff}
.m-hero .pill-badge{font-size:3.5px;padding:1px 4px}
.m-hero h1{font-family:var(--head);font-weight:800;font-size:12.5px;line-height:13.5px;letter-spacing:-.4px;margin-top:8px}
.m-hero h1 .grey{color:#8f96a3}
.m-hero h1 .mark{background:var(--lime);color:var(--ink);border-radius:3px;padding:0 2px}
.m-hero p{font-size:4.3px;line-height:6.5px;color:#c2c7d0;margin-top:6px}
.m-btn{height:15px;border-radius:8px;display:flex;align-items:center;justify-content:center;font-size:4.5px;font-weight:600;margin-top:7px}
.m-card{background:#fff;border:1px solid var(--line);border-radius:7px;padding:7px}
.m-sm{font-size:4px;color:var(--muted);line-height:5.5px}
.m-kick{font-size:3.8px;letter-spacing:.6px;font-weight:600;color:var(--muted)}
.m-chips{display:flex;flex-wrap:wrap;gap:3px;margin-top:5px}
.m-chips span{border:1px solid var(--line);border-radius:5px;padding:1px 4px;font-size:3.5px}
.m-title{font-family:var(--head);font-weight:700;font-size:9.5px;letter-spacing:-.2px}
.m-lab{font-size:3.5px;letter-spacing:1px;font-weight:600;color:#9ccf25}
.m-prod{background:#fff;border:1px solid var(--line);border-radius:7px;overflow:hidden}
.m-prod .visual{height:102px;position:relative}
.m-prod .tag{left:6px;top:5px;font-size:3.5px;padding:1px 4px}
.m-prod h3{font-family:var(--head);font-size:7.5px;line-height:9px;margin:9px 8px 0}
.m-prod p{font-size:4px;line-height:5.5px;color:var(--muted);margin:4px 8px 0}
.m-prod .pr{font-size:4.5px;font-weight:600;position:absolute;left:8px;bottom:8px}
.m-prod .rd{position:absolute;right:8px;bottom:5px;width:10px;height:10px;border:1px solid var(--line);border-radius:50%}
.m-step{text-align:center}
.m-step .n{width:24px;height:24px;border:1px solid var(--line);border-radius:50%;margin:0 auto;display:flex;align-items:center;justify-content:center;font-size:5px;font-weight:700}
.m-step b{display:block;font-size:5.5px;margin-top:9px}
.m-step span{display:block;font-size:4px;color:var(--muted);line-height:5.5px;margin-top:3px;padding:0 14px}
.m-feat{background:#fff;border:1px solid var(--line);border-radius:7px;padding:8px;height:68px}
.m-feat .badge{width:15px;height:15px;border-radius:4px;background:var(--ink)}
.m-feat b{display:block;font-size:5.5px;margin-top:8px}
.m-feat span{display:block;font-size:4px;color:var(--muted);line-height:5.5px;margin-top:3px}
.m-foot{position:absolute;left:0;top:2192px;width:156px;height:276px;background:var(--ink);color:#fff;padding:28px 10px}
.m-foot .row{border-bottom:1px solid #2a3040;font-size:4.5px;font-weight:700;padding:6px 0;display:flex;justify-content:space-between}
</style>
</head>
<body>
<div class="stage">

<!-- ================= MOBILE ================= -->
<div class="mob">
  <div class="m m-nav"><div class="brand">printfeld<span class="dot"></span></div><span class="btn btn-dark">Editor öffnen ↗</span><span style="margin-left:5px;font-size:7px">≡</span></div>

  <div class="m m-hero">
    <span class="pill-badge"><i></i>Neuer Printfeld-Editor · v2.4</span>
    <h1>Druckprodukte.<br><span class="grey">Online gestalten.</span><br><span class="mark">Ohne E-Mail.</span></h1>
    <p>Logo hochladen, Text setzen, Vorder- und Rückseite prüfen — und absenden. Wir prüfen jede Datei persönlich vor dem Druck.</p>
    <div class="m-btn btn-lime">Editor öffnen ↗</div>
    <div class="m-btn" style="border:1px solid #3a4050;margin-top:5px">⇪ Datei hochladen</div>
  </div>

  <div class="m m-card" style="top:215px;width:64px;height:63px"><div class="m-kick">BEWERTUNG</div><div style="font-size:5px;margin-top:10px">★★★★★</div><div style="font-family:var(--head);font-weight:700;font-size:10px">4,9</div><div class="m-sm">von 380 Kunden</div></div>
  <div class="m" style="top:215px;left:82px;width:64px;height:63px;background:var(--lime);border-radius:7px;padding:7px"><div class="m-kick" style="color:#4d6312">PRÜFUNG</div><div style="font-family:var(--head);font-weight:700;font-size:10px;margin-top:5px">100%</div><div class="m-sm" style="color:var(--ink)">der Druckdaten persönlich geprüft, bevor produziert wird.</div></div>

  <div class="m m-card" style="top:286px;height:84px"><div class="m-kick">IM EDITOR VERFÜGBAR</div><div class="m-chips"><span>T Text</span><span>Logo Upload</span><span>Formen</span><span>Farben</span><span>Drag &amp; Drop</span><span>Vorlagen</span></div><div style="font-size:3.8px;color:#8fbf1a;margin-top:12px">Editor live ausprobieren →</div></div>

  <div class="m" style="top:396px"><div class="m-lab">01 — PRODUKTE</div><div class="m-title" style="margin-top:5px">Was möchten Sie drucken?</div></div>

  <div class="m m-prod" style="top:435px;height:171px"><div class="visual v-bag" role="img" aria-label="Papierbeutel mit Logo-Aufdruck"><span class="tag">Verpackung</span></div><h3>Papierbeutel<br>&amp; Taschen</h3><p>Standbodenbeutel, Tragetaschen, mit oder ohne Fenster.</p><span class="pr">ab CHF 1.20</span><span class="rd"></span></div>
  <div class="m m-prod" style="top:623px;height:180px"><div class="visual v-plate" role="img" aria-label="Ovale Stallplakette in Rosa"><span class="tag">Pferdesport</span></div><h3>Stallplaketten<br>&amp; Schilder</h3><p>Holz, Aluminium, oval oder eckig — mit Wunschtext.</p><span class="pr">ab CHF 24.00</span><span class="rd"></span></div>
  <div class="m m-prod" style="top:811px;height:173px"><div class="visual v-misc" role="img" aria-label="Laternen und Marken in Lila"><span class="tag">Diverses</span></div><h3>Laternen, Marken<br>&amp; mehr</h3><p>Personalisierte Laser- und Druckprodukte.</p><span class="pr">ab CHF 14.90</span><span class="rd"></span></div>

  <div class="m m-card" style="top:1013px;height:395px;text-align:center;padding-top:9px">
    <div class="m-lab">02 — ABLAUF</div>
    <div class="m-title" style="margin-top:4px;font-size:8.5px">In 4 Schritten zur<br>Druckdatei.</div>
    <div class="m-sm" style="margin-top:6px;padding:0 10px">Vom Produkt zur fertigen Druckdatei — geführt, geprüft, ohne Umwege.</div>
    <div class="m-step" style="margin-top:10px"><div class="n">01</div><b>Produkt wählen</b><span>Aus dem Katalog auswählen und Variante festlegen.</span></div>
    <div class="m-step" style="margin-top:12px"><div class="n">02</div><b>Gestalten oder hochladen</b><span>Editor öffnen oder fertige Druckdatei hochladen.</span></div>
    <div class="m-step" style="margin-top:12px"><div class="n">03</div><b>Vorder- + Rückseite prüfen</b><span>Beide Seiten separat kontrollieren in der Vorschau.</span></div>
    <div class="m-step" style="margin-top:12px"><div class="n">04</div><b>Absenden &amp; geniessen</b><span>Wir prüfen die Daten persönlich und drucken.</span></div>
  </div>

  <div class="m" style="top:1433px;text-align:center"><div class="m-lab">03 — EDITOR</div><div class="m-title" style="margin-top:4px;font-size:8.5px">Direkt im Browser<br>gestalten.</div><div class="m-sm" style="margin-top:5px;padding:0 4px">Kein Mockup — das ist der echte Editor. Probier ihn gleich hier aus.</div><div class="m-btn btn-dark" style="margin-top:7px">Vollbild öffnen ↗</div></div>

  <div class="m m-card" style="top:1529px;height:264px;padding:4px;background:#edeff2">
    <div style="background:#fff;height:22px;margin:-4px -4px 0;border-radius:7px 7px 0 0;font-size:3.5px;padding:3px 6px;color:var(--muted)">Vorderseite · Rückseite · 100% · Vorschau</div>
    <div style="font-size:3px;color:var(--muted);margin-top:3px">210 × 297 mm · 3 mm Beschnitt</div>
    <div style="background:#fff;height:178px;margin:3px 2px 0;position:relative">
      <div style="position:absolute;left:12px;top:26px;font-size:3.5px;font-weight:700">FELLCHEN</div>
      <div style="position:absolute;left:44px;top:17px;width:38px;height:38px;border-radius:50%;background:#c4f25c"></div>
      <div style="position:absolute;left:14px;top:102px;width:92px;height:22px;border:1px solid var(--ink);font-family:var(--head);font-weight:700;font-size:6.5px;text-align:center;line-height:7px;padding-top:3px">Premium<br>Hauptfutter</div>
    </div>
    <div style="font-size:3px;background:#fff;border-radius:4px;display:inline-block;padding:1px 4px;margin-top:6px">• Live · Vorderseite · Druckbereich sichtbar</div>
    <div style="position:absolute;left:0;right:0;bottom:0;height:22px;background:#fff;display:flex;justify-content:space-around;align-items:center;font-size:3.2px;color:var(--muted);border-radius:0 0 7px 7px"><span>Werkzeuge</span><span>Ebenen (4)</span><span>Eigenschaften</span></div>
  </div>

  <div class="m m-feat" style="top:1819px"><div class="badge"></div><b>Persönliche Datenprüfung</b><span>Jede Druckdatei wird vor dem Druck geprüft — keine bösen Überraschungen.</span></div>
  <div class="m m-feat" style="top:1896px"><div class="badge"></div><b>Upload als Alternative</b><span>Fertige Datei? Direkt hochladen. Kein Editor-Zwang.</span></div>
  <div class="m m-feat" style="top:1973px"><div class="badge"></div><b>Schweizer Druckpartner</b><span>Lokale Produktion, geprüfte Materialien, faire Preise.</span></div>

  <div class="m" style="top:2068px;left:7px;width:142px;height:96px;background:var(--lime);border-radius:8px;padding:12px 12px">
    <div class="m-title" style="font-size:9px;line-height:10px">Bereit, dein Produkt zu gestalten?</div>
    <div class="m-btn btn-dark" style="margin-top:6px">Editor öffnen ↗</div>
    <div class="m-btn" style="border:1px solid var(--ink);margin-top:6px">Produkte ansehen</div>
  </div>

  <div class="m-foot">
    <div class="brand" style="font-size:12px">printfeld<span class="dot" style="width:5px;height:5px"></span></div>
    <div style="font-size:4px;color:#aeb4bf;line-height:6px;margin-top:6px">Druckprodukte online gestalten — Editor, Upload und persönliche Datenprüfung. Lokale Produktion in der Schweiz.</div>
    <div class="m-btn btn-lime" style="width:58px;height:12px;margin-top:6px">Editor öffnen ↗</div>
    <div style="margin-top:12px"><div class="row"><span>Produkte</span><span>⌄</span></div><div class="row"><span>Service</span><span>⌄</span></div><div class="row"><span>Unternehmen</span><span>⌄</span></div></div>
    <div style="font-size:4.5px;font-weight:700;margin-top:16px">Kontakt</div>
    <div style="font-size:4px;color:#aeb4bf;line-height:8px;margin-top:4px">✉ hallo@printfeld.ch<br>✆ +41 44 123 45 67<br>⌖ Musterweg 12<br>&nbsp;&nbsp;&nbsp;8000 Zürich</div>
    <div style="font-size:3.5px;color:#7d8593;margin-top:22px">© 2026 printfeld. Alle Rechte vorbehalten.</div>
  </div>
</div>

<!-- ================= DESKTOP ================= -->
<div class="desk">
  <header class="abs nav">
    <div class="brand">printfeld<span class="dot"></span></div>
    <nav class="nav-links"><span>Produkte</span><span>Editor</span><span>Beispiel</span><span>Kontakt</span></nav>
    <span class="icon-btn"><svg class="ico" viewBox="0 0 24 24"><circle cx="11" cy="11" r="7"/><path d="M20 20l-4-4"/></svg></span>
    <span class="btn btn-dark" style="height:22px">Editor öffnen <svg class="ico" style="width:7px;height:7px" viewBox="0 0 24 24"><path d="M7 17L17 7M8 7h9v9"/></svg></span>
  </header>

  <section class="abs hero">
    <span class="pill-badge"><i></i>Neuer Printfeld-Editor · v2.4</span>
    <h1>Druckprodukte.<br><span class="grey">Online gestalten.</span><br><span class="mark">Ohne E-Mail.</span></h1>
    <p>Logo hochladen, Text setzen, Vorder- und Rückseite prüfen — und absenden. Wir prüfen jede Datei persönlich vor dem Druck.</p>
    <div class="actions">
      <span class="btn btn-lime">Editor öffnen <span class="arrow-dot"><svg class="ico" viewBox="0 0 24 24"><path d="M7 17L17 7M8 7h9v9"/></svg></span></span>
      <span class="btn btn-ghost"><svg class="ico" viewBox="0 0 24 24"><path d="M12 15V4M7 9l5-5 5 5M4 16v4h16v-4"/></svg>Datei hochladen</span>
    </div>
  </section>

  <div class="abs mini-card" style="left:536px;top:82px;width:145px;height:135px">
    <div class="kicker">Bewertung</div>
    <div class="stars">★★★★★</div>
    <div class="big-num">4,9</div>
    <div class="small">von 380 Kunden</div>
  </div>
  <div class="abs check-card" style="left:697px;top:82px;width:147px;height:135px">
    <div class="kicker">Prüfung</div>
    <div class="big-num">100%</div>
    <div class="small">der Druckdaten persönlich geprüft, bevor produziert wird.</div>
  </div>
  <div class="abs mini-card" style="left:536px;top:234px;width:308px;height:164px">
    <div class="kicker">Im Editor verfügbar</div>
    <div class="chips">
      <span class="chip"><svg class="ico" viewBox="0 0 24 24"><path d="M5 5h14M12 5v14"/></svg>Text</span>
      <span class="chip"><svg class="ico" viewBox="0 0 24 24"><rect x="4" y="4" width="16" height="16" rx="2"/><path d="M4 16l5-5 5 5 3-3 3 3"/></svg>Logo Upload</span>
      <span class="chip"><svg class="ico" viewBox="0 0 24 24"><rect x="5" y="5" width="14" height="14" rx="2"/></svg>Formen</span>
      <span class="chip"><svg class="ico" viewBox="0 0 24 24"><circle cx="12" cy="12" r="8"/><circle cx="9" cy="10" r="1"/><circle cx="14" cy="9" r="1"/></svg>Farben</span>
      <span class="chip"><svg class="ico" viewBox="0 0 24 24"><path d="M5 4l14 6-6 2-2 6z"/></svg>Drag &amp; Drop</span>
      <span class="chip"><svg class="ico" viewBox="0 0 24 24"><path d="M12 3v5M12 16v5M3 12h5M16 12h5"/></svg>Vorlagen</span>
    </div>
    <div class="lime-link">Editor live ausprobieren →</div>
  </div>

  <section class="abs prod-head">
    <div class="sec-label">01 — PRODUKTE</div>
    <h2 class="sec-title">Was möchten Sie drucken?</h2>
    <span class="all-link">Alle Produkte →</span>
  </section>
  <section class="abs products">
    <article class="product">
      <div class="visual v-bag" role="img" aria-label="Gelber Papierbeutel mit Logo-Aufdruck"><span class="tag">Verpackung</span></div>
      <h3>Papierbeutel<br>&amp; Taschen</h3>
      <p>Standbodenbeutel, Tragetaschen, mit oder ohne Fenster.</p>
      <span class="price">ab CHF 1.20</span>
      <span class="round"><svg class="ico" viewBox="0 0 24 24"><path d="M7 17L17 7M8 7h9v9"/></svg></span>
    </article>
    <article class="product">
      <div class="visual v-plate" role="img" aria-label="Ovale rosa Stallplakette mit Namen"><span class="tag">Pferdesport</span></div>
      <h3>Stallplaketten<br>&amp; Schilder</h3>
      <p>Holz, Aluminium, oval oder eckig — mit Wunschtext.</p>
      <span class="price">ab CHF 24.00</span>
      <span class="round"><svg class="ico" viewBox="0 0 24 24"><path d="M7 17L17 7M8 7h9v9"/></svg></span>
    </article>
    <article class="product">
      <div class="visual v-misc" role="img" aria-label="Laterne und Marke in Lila und Blau"><span class="tag">Diverses</span></div>
      <h3>Laternen, Marken<br>&amp; mehr</h3>
      <p>Personalisierte Laser- und Druckprodukte.</p>
      <span class="price">ab CHF 14.90</span>
      <span class="round"><svg class="ico" viewBox="0 0 24 24"><path d="M7 17L17 7M8 7h9v9"/></svg></span>
    </article>
  </section>

  <section class="abs steps">
    <div class="sec-label">02 — ABLAUF</div>
    <h2 class="sec-title" style="font-size:21px">In 4 Schritten zur Druckdatei.</h2>
    <p class="aside">Vom Produkt zur fertigen Druckdatei — geführt, geprüft, ohne Umwege.</p>
    <div class="track"></div>
    <div class="step" style="left:25px"><div class="num">01</div><h4>Produkt wählen</h4><p>Aus dem Katalog auswählen und Variante festlegen.</p></div>
    <div class="step" style="left:206px"><div class="num">02</div><h4>Gestalten oder hochladen</h4><p>Editor öffnen oder fertige Druckdatei hochladen.</p></div>
    <div class="step" style="left:388px"><div class="num">03</div><h4>Vorder- + Rückseite prüfen</h4><p>Beide Seiten separat kontrollieren in der Vorschau.</p></div>
    <div class="step" style="left:569px"><div class="num">04</div><span class="done">FERTIG</span><h4>Absenden &amp; geniessen</h4><p>Wir prüfen die Daten persönlich und drucken.</p></div>
  </section>

  <section class="abs ed-head">
    <div class="sec-label">03 — EDITOR</div>
    <h2 class="sec-title" style="font-size:21px">Direkt im Browser gestalten.</h2>
    <p class="sec-sub">Kein Mockup — das ist der echte Editor. Probier ihn gleich hier aus.</p>
    <span class="btn btn-dark">Vollbild öffnen ↗</span>
  </section>

  <section class="abs editor">
    <div class="ed-left">
      <div style="padding:10px 9px 12px;border-bottom:1px solid var(--line)">
        <div class="ed-label">HINZUFÜGEN</div>
        <div class="tools">
          <div class="tool"><svg class="ico" viewBox="0 0 24 24"><path d="M5 5h14M12 5v14"/></svg>Text</div>
          <div class="tool"><svg class="ico" viewBox="0 0 24 24"><rect x="4" y="4" width="16" height="16" rx="2"/><path d="M4 16l5-5 5 5"/></svg>Bild</div>
          <div class="tool"><svg class="ico" viewBox="0 0 24 24"><rect x="5" y="5" width="14" height="14" rx="2"/></svg>Form</div>
          <div class="tool on"><svg class="ico" viewBox="0 0 24 24"><path d="M12 15V4M7 9l5-5 5 5M4 16v4h16v-4"/></svg>Upload</div>
        </div>
      </div>
      <div style="padding:10px 9px;border-bottom:1px solid var(--line)">
        <div class="ed-label">HINTERGRUND</div>
        <div class="swatches"><i class="sw" style="background:#fff;border:1.5px solid var(--lime)"></i><i class="sw" style="background:#f1e6d8"></i><i class="sw" style="background:var(--ink)"></i><i class="sw" style="background:#fbefc4"></i><i class="sw" style="background:#dbe7fb"></i></div>
      </div>
      <div style="padding:10px 9px 6px"><div class="ed-label">◈ EBENEN (4)</div></div>
      <div class="layer"><b>T</b>1.2 kg · natürlich · sch…</div>
      <div class="layer on"><b>T</b>Premium</div>
      <div class="layer"><b>▢</b>Form</div>
      <div class="layer"><b>T</b>FELLCHEN</div>
    </div>

    <div class="ed-mid">
      <div class="ed-bar">
        <div class="seg"><span class="on">Vorderseite</span><span>Rückseite</span></div>
        <span>↶</span><span>↷</span>
        <span style="background:var(--lime-soft);padding:4px 7px;border-radius:6px">▦ Hilfslinien</span>
        <span style="margin-left:auto">⊖</span><span style="font-weight:600">100%</span><span>⊕</span>
        <span class="btn btn-dark" style="height:18px;padding:0 9px;font-size:7.5px">Vorschau</span>
      </div>
      <div class="abs" style="left:108px;top:98px;font-size:6px;color:var(--muted)">210 × 297 mm · 3 mm Beschnitt</div>
      <div class="page">
        <div class="inner"></div>
        <div class="abs" style="left:19px;top:57px;font-size:7px;font-weight:700;letter-spacing:.3px">FELLCHEN</div>
        <div class="abs" style="left:92px;top:38px;width:60px;height:60px;border-radius:50%;background:#c4f25c"></div>
        <div class="abs" style="left:-13px;top:260px;font-size:4.5px;color:var(--muted)">1.2 kg · natürlich · schweizer herkunft</div>
      </div>
      <div class="sel" style="left:85px">Premium<br>Hauptfutter<b style="left:-3px;top:-3px"></b><b style="right:-3px;top:-3px"></b><b style="left:-3px;bottom:-3px"></b><b style="right:-3px;bottom:-3px"></b></div>
      <div class="live"><i></i>Live · Vorderseite · Druckbereich sichtbar</div>
    </div>

    <div class="ed-right">
      <div style="height:32px;display:flex;align-items:center;border-bottom:1px solid var(--line);margin:0 -10px;padding:0 10px"><span class="ed-label" style="font-size:7px">TEXT</span><span style="margin-left:auto;font-size:8px;color:var(--muted)">⧉</span><svg class="ico" style="margin-left:10px;width:9px;height:9px;color:#e24a4a" viewBox="0 0 24 24"><path d="M4 7h16M9 7V4h6v3M6 7l1 13h10l1-13"/></svg></div>
      <div class="pl" style="margin-top:14px">TEXT</div>
      <div class="field" style="height:40px;align-items:flex-start;padding-top:5px;line-height:9px">Premium<br>Hauptfutter</div>
      <div class="pl" style="margin-top:14px">SCHRIFT</div>
      <div class="field">Feldgrotesk<span style="margin-left:auto">⌄</span></div>
      <div style="display:flex;gap:6px;margin-top:13px"><div style="flex:1"><div class="pl">GRÖSSE</div><div class="field">22</div></div><div style="flex:1"><div class="pl">GEWICHT</div><div class="field">Bold</div></div></div>
      <div class="pl" style="margin-top:13px">AUSRICHTUNG</div>
      <div class="field" style="justify-content:space-around;padding:0"><span>≡</span><span style="background:#eef0f3;padding:2px 16px">≡</span><span>≡</span></div>
      <div class="pl" style="margin-top:13px">STIL</div>
      <div style="display:flex;gap:6px;margin-top:5px;font-size:7px"><span style="width:18px;height:18px;border-radius:50%;background:var(--lime-soft);border:1px solid var(--lime);display:flex;align-items:center;justify-content:center;font-weight:700">B</span><span style="width:18px;height:18px;display:flex;align-items:center;justify-content:center;font-style:italic">I</span></div>
      <div class="pl" style="margin-top:13px">FARBE</div>
      <div class="dots"><i style="background:var(--ink);outline:1.5px solid var(--lime);outline-offset:1px"></i><i style="background:#6b6cf0"></i><i style="background:#2fbf5a"></i><i style="background:#e8453c"></i><i style="background:#f59e0b"></i><i style="background:#ec4899"></i><i style="background:#0ea5e9"></i><i style="background:#fff;border:1px solid var(--line)"></i><i style="border:1px solid var(--line)"></i></div>
      <div style="display:flex;gap:6px;margin-top:12px"><div style="flex:1"><div class="pl">X (%)</div><div class="field">60</div></div><div style="flex:1"><div class="pl">Y (%)</div><div class="field">70</div></div></div>
      <div style="display:flex;gap:6px;margin-top:10px"><div style="flex:1"><div class="pl">BREITE (%)</div><div class="field">70</div></div><div style="flex:1"><div class="pl">ROTATION</div><div class="field">↻&nbsp; 0</div></div></div>
    </div>
  </section>

  <section class="abs features">
    <div class="feat"><span class="badge"><svg class="ico" viewBox="0 0 24 24"><path d="M12 3l7 3v6c0 4-3 7-7 9-4-2-7-5-7-9V6z"/><path d="M9 12l2 2 4-4"/></svg></span><h4>Persönliche Datenprüfung</h4><p>Jede Druckdatei wird vor dem Druck geprüft — keine bösen Überraschungen.</p></div>
    <div class="feat"><span class="badge"><svg class="ico" viewBox="0 0 24 24"><path d="M12 15V4M7 9l5-5 5 5M4 16v4h16v-4"/></svg></span><h4>Upload als Alternative</h4><p>Fertige Datei? Direkt hochladen. Kein Editor-Zwang.</p></div>
    <div class="feat"><span class="badge"><svg class="ico" viewBox="0 0 24 24"><path d="M12 4l1.5 4.5L18 10l-4.5 1.5L12 16l-1.5-4.5L6 10l4.5-1.5zM18 16l.7 2 2 .7-2 .7-.7 2-.7-2-2-.7 2-.7z"/></svg></span><h4>Schweizer Druckpartner</h4><p>Lokale Produktion, geprüfte Materialien, faire Preise.</p></div>
  </section>

  <section class="abs cta">
    <h2>Bereit, dein Produkt zu gestalten?</h2>
    <div class="actions"><span class="btn btn-dark">Editor öffnen ↗</span><span class="btn btn-outline">Produkte ansehen</span></div>
  </section>

  <footer class="abs foot">
    <div class="brand">printfeld<span class="dot"></span></div>
    <p class="desc">Druckprodukte online gestalten — Editor, Upload und persönliche Datenprüfung. Lokale Produktion in der Schweiz.</p>
    <span class="btn btn-lime">Editor öffnen ↗</span>
    <div class="fcol" style="left:399px"><h5>Produkte</h5><div>Papierbeutel</div><div>Stallplaketten</div><div>Laternen</div><div>Hundemarken</div><div>Alle Produkte</div></div>
    <div class="fcol" style="left:505px"><h5>Service</h5><div>Editor öffnen</div><div>Datei hochladen</div><div>Datenprüfung</div><div>Versand</div><div>Kontakt</div></div>
    <div class="fcol" style="left:611px"><h5>Unternehmen</h5><div>Über uns</div><div>Druckpartner</div><div>Nachhaltigkeit</div><div>Impressum</div><div>Datenschutz</div></div>
    <div class="fcol" style="left:728px"><h5>Kontakt</h5>
      <div><svg class="ico" viewBox="0 0 24 24"><rect x="3" y="5" width="18" height="14" rx="2"/><path d="M3 7l9 6 9-6"/></svg>hallo@printfeld.ch</div>
      <div><svg class="ico" viewBox="0 0 24 24"><path d="M5 4h4l2 5-3 2a11 11 0 0 0 5 5l2-3 5 2v4a2 2 0 0 1-2 2A16 16 0 0 1 3 6a2 2 0 0 1 2-2"/></svg>+41 44 123 45 67</div>
      <div><svg class="ico" viewBox="0 0 24 24"><path d="M12 21s-7-6-7-11a7 7 0 0 1 14 0c0 5-7 11-7 11z"/><circle cx="12" cy="10" r="2.5"/></svg>Musterweg 12<br>8000 Zürich</div>
    </div>
    <div class="bottom"><span>© 2026 printfeld. Alle Rechte vorbehalten.</span><span style="margin-left:auto">Impressum</span><span>Datenschutz</span><span>AGB</span></div>
  </footer>
</div>

</div>
</body>
</html>
```